packaging design for a hair accessories brand called VOSSIE KIT

Vossie Kit is a premium hair accessories brand focused on elevated everyday style through beautifully crafted pieces that combine fashion, durability, and craftsmanship.

All products are handmade using high-quality materials and are designed to be exceptionally resistant, long-lasting, and almost unbreakable while still feeling elegant and refined.
The brand is not minimalist. Instead, it embraces a sophisticated and distinctive aesthetic with strong attention to detail, texture, shape, and presentation. The packaging and visual identity should feel modern, polished, feminine, and fashion-forward without looking overly simple or basic.Target customer:
Women 25–45 who care about personal style, quality, and details. They appreciate products that feel special, elevated, durable, and thoughtfully designed. They enjoy fashion and beauty products that look premium and giftable while remaining functional for everyday use.
The brand is for Mexico, so the text should be in spanish.
Brands for reference: Quorvade, brelto, The tress nook
The visual identity should communicate:
Elegance
Premium craftsmanship
High quality
Durability
Sophistication
Modern femininity
Fashion-forward style
Boutique aesthetic

The packaging should feel:
Elegant and elevated
Visually rich and refined
Premium and giftable
Stylish and memorable
Sophisticated without being overly luxurious
Fashion-oriented and feminine
Designers should also develop a custom typography direction and logo treatment for the brand. The typography should feel distinctive, elegant, modern, and recognizable, helping create a strong brand identity that can extend across packaging, tags, and digital platforms.
The final visual identity should work cohesively across:
Hair accessory packaging
Hang tags
Product cards
Boxes and gift sets
E-commerce packaging
Social media and branding materials

I attach a packaging for reference. Use front and back. Measurments are: 10.5 xm x 13.5 cm

```html
<!DOCTYPE html>
<html lang="es">
<head>
<meta charset="UTF-8">
<title>Vossie Kit — Empaque frente y reverso</title>
<link href="https://fonts.googleapis.com/css2?family=Josefin+Sans:wght@300;400;600&family=Allura&display=swap" rel="stylesheet">
<style>
  :root{
    --bg:#ebe2d8;
    --card-edge:#2f2c2c;
    --cream:#f4ece3;
    --ink:#3a2327;
    --wine:#7a2340;
    --wine-soft:#b98a96;
    --clip-a:#a3174e;
    --clip-b:#6b0c31;
    --floral-a:#efe2dc;
    --floral-b:#e3cfcf;
    --hanger:#f6f2ee;
  }
  *{box-sizing:border-box;margin:0;padding:0}
  html,body{width:932px;height:1200px;overflow:hidden;background:var(--bg)}
  body{position:relative;font-family:"Josefin Sans",sans-serif;color:var(--ink)}

  .hang-tab{position:absolute;width:164px;height:66px;background:var(--hanger);
    border:1px solid #ddd4cb;border-bottom:none;border-radius:6px 6px 0 0}
  .hang-tab .slot{position:absolute;left:30px;right:30px;top:24px;height:22px;
    border:1px solid #d6ccc3;border-radius:12px 12px 4px 4px}

  .card{position:absolute;background:var(--card-edge);border-radius:20px;padding:12px}
  .card-face{position:relative;width:100%;height:100%;background:var(--cream);border-radius:10px;overflow:hidden}
  .card--front{left:30px;top:118px;width:426px;height:1003px}
  .card--back{left:486px;top:126px;width:406px;height:995px}

  .frame-line{position:absolute;left:16px;right:16px;top:16px;bottom:16px;border:1px solid var(--wine-soft);border-radius:4px}

  .centered{position:absolute;left:0;right:0;text-align:center}
  .sparkle{position:absolute}
  .wordmark{font-weight:300;font-size:46px;letter-spacing:3px;color:var(--ink);line-height:1}
  .wordmark-sub{display:flex;align-items:center;justify-content:center;gap:12px;
    font-size:17px;letter-spacing:10px;font-weight:300}
  .wordmark-sub::before,.wordmark-sub::after{content:"";width:42px;height:1px;background:var(--ink)}
  .category{font-size:11px;letter-spacing:3.2px}

  .product-photo{position:absolute;left:88px;top:218px;width:326px;height:568px;
    border-radius:60px 40px 70px 40px;background:linear-gradient(150deg,var(--clip-a),var(--clip-b))}
  .floral{position:absolute;background:linear-gradient(180deg,var(--floral-a),var(--floral-b),var(--floral-a));border-radius:40px}

  .dash-rule{position:absolute;left:69px;top:590px;height:253px;border-left:1px dashed var(--wine)}
  .monogram{position:absolute;left:192px;top:836px;width:40px;height:40px;border:1.5px solid var(--wine);transform:rotate(45deg)}
  .tagline{font-size:13px;letter-spacing:2.4px;color:var(--wine)}
  .script{font-family:"Allura",cursive;color:var(--wine)}

  .intro{font-size:15px;line-height:21.5px;font-weight:400}
  .divider{position:absolute;left:88px;width:218px;display:flex;align-items:center;gap:10px}
  .divider::before,.divider::after{content:"";flex:1;height:1px;background:var(--ink)}

  .feature{position:absolute;left:88px;width:240px;display:flex;gap:22px}
  .feature .icon{width:38px;height:38px;flex:none;color:var(--ink)}
  .feature h3{font-size:13px;font-weight:400;letter-spacing:.8px;margin-bottom:3px}
  .feature h3.accent{color:var(--wine)}
  .feature p{font-size:13px;line-height:17px}

  .discover{font-size:13px;letter-spacing:1.6px;color:var(--wine)}
  .social-row{display:flex;justify-content:center;align-items:center;gap:14px;font-size:12.5px}
  .social-item{display:flex;align-items:center;gap:8px}
  .social-dot{width:16px;height:16px;border:1.5px solid var(--ink);border-radius:50%}
  .social-sep{width:1px;height:16px;background:var(--ink);margin:0 8px}
  .origin{font-size:13px;letter-spacing:2px}
</style>
</head>
<body>

  <div class="hang-tab" style="left:170px;top:54px"><span class="slot"></span></div>
  <div class="hang-tab" style="left:600px;top:56px"><span class="slot"></span></div>

  <!-- FRONT -->
  <section class="card card--front" aria-label="Frente del empaque">
    <div class="card-face">
      <div class="frame-line"></div>

      <svg class="sparkle" style="left:193px;top:34px" width="18" height="22" viewBox="0 0 18 22"><path d="M9 0 L11 9 L18 11 L11 13 L9 22 L7 13 L0 11 L7 9 Z" fill="var(--ink)"/></svg>
      <div class="centered wordmark" style="top:72px">VOSSIE</div>
      <div class="centered wordmark-sub" style="top:130px">KIT</div>
      <div class="centered category" style="top:176px">ACCESORIOS PARA EL CABELLO</div>

      <div class="product-photo" role="img" aria-label="Fotografía de pinza para el cabello color vino brillante"></div>
      <div class="floral" style="left:4px;top:397px;width:80px;height:337px" role="img" aria-label="Ilustración floral de línea en tono vino"></div>

      <svg class="sparkle" style="left:61px;top:566px" width="16" height="20" viewBox="0 0 18 22"><path d="M9 0 L11 9 L18 11 L11 13 L9 22 L7 13 L0 11 L7 9 Z" fill="var(--wine)"/></svg>
      <div class="dash-rule"></div>

      <div class="monogram" aria-hidden="true"></div>
      <div class="centered tagline" style="top:900px">DISEÑADOS PARA DURAR.</div>
      <div class="centered script" style="top:918px;font-size:28px">Hechos para brillar.</div>
    </div>
  </section>

  <!-- BACK -->
  <section class="card card--back" aria-label="Reverso del empaque">
    <div class="card-face">
      <svg class="sparkle" style="left:183px;top:34px" width="18" height="22" viewBox="0 0 18 22"><path d="M9 0 L11 9 L18 11 L11 13 L9 22 L7 13 L0 11 L7 9 Z" fill="var(--ink)"/></svg>
      <div class="centered wordmark" style="top:72px">VOSSIE</div>
      <div class="centered wordmark-sub" style="top:128px">KIT</div>
      <div class="centered category" style="top:168px">ACCESORIOS PARA EL CABELLO</div>

      <p class="centered intro" style="top:206px">Cada pieza está hecha a mano<br>con materiales de alta calidad,<br>diseñada para acompañarte todos<br>los días con estilo, resistencia<br>y un toque de elegancia.</p>

      <div class="divider" style="top:342px"><svg width="14" height="16" viewBox="0 0 18 22"><path d="M9 0 L11 9 L18 11 L11 13 L9 22 L7 13 L0 11 L7 9 Z" fill="var(--ink)"/></svg></div>

      <div class="floral" style="left:362px;top:291px;width:40px;height:417px" role="img" aria-label="Ilustración floral de línea en tono vino"></div>

      <div class="feature" style="top:388px">
        <svg class="icon" viewBox="0 0 40 40" fill="none" stroke="currentColor" stroke-width="1.4"><path d="M6 14 L12 6 H28 L34 14 L20 34 Z M6 14 H34 M12 6 L16 14 L20 34 L24 14 L28 6 M16 14 L20 6 L24 14"/></svg>
        <div><h3>HECHO A MANO</h3><p>Con atención a cada detalle.</p></div>
      </div>
      <div class="feature" style="top:462px">
        <svg class="icon" viewBox="0 0 40 40" fill="none" stroke="var(--wine)" stroke-width="1.6"><rect x="5" y="17" width="18" height="10" rx="5" transform="rotate(-45 14 22)"/><rect x="17" y="13" width="18" height="10" rx="5" transform="rotate(-45 26 18)"/></svg>
        <div><h3 class="accent">EXTRA RESISTENTE</h3><p>Materiales premium,<br>casi irrompibles.</p></div>
      </div>
      <div class="feature" style="top:542px">
        <svg class="icon" viewBox="0 0 40 40" fill="none" stroke="currentColor" stroke-width="1.3"><path d="M10 4 L11.5 9 L16 10 L11.5 11 L10 16 L8.5 11 L4 10 L8.5 9 Z"/><path d="M26 12 L28 19 L35 21 L28 23 L26 30 L24 23 L17 21 L24 19 Z"/><path d="M12 26 L13 30 L17 31 L13 32 L12 36 L11 32 L7 31 L11 30 Z"/></svg>
        <div><h3 class="accent">ACABADO PREMIUM</h3><p>Brillo, color y textura<br>que perduran.</p></div>
      </div>
      <div class="feature" style="top:631px">
        <svg class="icon" viewBox="0 0 40 40" fill="none" stroke="currentColor" stroke-width="1.4"><circle cx="20" cy="20" r="15"/></svg>
        <div><h3>DISEÑO QUE ELEVA<br>TU ESTILO</h3><p>Elegancia en cada detalle.</p></div>
      </div>

      <div class="divider" style="top:728px"><svg width="14" height="16" viewBox="0 0 18 22"><path d="M9 0 L11 9 L18 11 L11 13 L9 22 L7 13 L0 11 L7 9 Z" fill="var(--ink)"/></svg></div>

      <div class="centered discover" style="top:763px">DESCUBRE MÁS</div>
      <div class="centered social-row" style="top:794px">
        <span class="social-item"><span class="social-dot"></span>@vossie.kit</span>
        <span class="social-sep"></span>
        <span class="social-item"><span class="social-dot"></span>vossiekit.mx</span>
      </div>

      <div class="centered script" style="top:856px;font-size:21px">Gracias por elegir lo hecho con amor.</div>
      <div class="centered origin" style="top:916px">HECHO EN MÉXICO</div>
      <svg class="centered" style="top:944px;margin:0 auto" width="14" height="13" viewBox="0 0 24 22"><path d="M12 20 C4 14 2 10 2 7 A5 5 0 0 1 12 5 A5 5 0 0 1 22 7 C22 10 20 14 12 20 Z" fill="none" stroke="var(--ink)" stroke-width="2"/></svg>
    </div>
  </section>

</body>
</html>
```